Quirky Label Design for an Exciting UK-Based Organic Skincare Company!

We need label designs across our range of products, we are a high quality yet quirky organic skincare company called Gently Lumora, we use frosted glass packaging, and we are just wanting one design done for now, but the winning designer we would want to work with to design the rest of the labels for us. We also want them to design business cards and other literature at some point and maybe even a website page.

Our label design will go on a 63mm tall frosted glass jar which is 62mm in diameter. The actual label dimensions should be, 170 mm (W) x 50 mm (H). The idea is so that it wraps around the whole jar with the design at one side (at the front) and the ingredients on another (at the back).

LABEL 1
Organic Polynesian Whipped Body Butter
Vanilla Bean
120ml

Made with Organic Shea and Cocoa Butters and exotic Monoi de Tahiti

Ingredients (INCI): Organic Raw Shea Butter (Butyrospermum Parkii), Organic Raw Cocoa Butter (Theobroma Cacao), Monoi de Tahiti (Coconut (Cocos nucifera) oil (and) Tiare (Gardenia tahitensis) flower), Organic Sweet Almond Oil (Prunus Amygdalus Dulcis), Organic Madagascan Vanilla Extract (Vanillin)

Handmade by Gently Lumora Ltd
14 Quillfield Lane, Bournemouth BH2 9RT, UK
Batch:

OPTIONAL WRITING (if it fits in):
100% Natural and Organic
Intensely Moisturising

LABEL 2
Mango Smoothie
120ml

Ingredients (INCI): Organic Raw Shea Butter (Butyrospermum Parkii), Organic Raw Cocoa Butter (Theobroma Cacao), Monoi de Tahiti (Coconut (Cocos nucifera) oil (and) Tiare (Gardenia tahitensis) flower), Organic Sweet Almond Oil (Prunus Amygdalus Dulcis), Organic Mango Flavour (Aroma)

Batch:

100% Natural and Organic
Intensely Moisturising

I have attached a picture of the jar we use and the lid we use for these products, as well as our logo. I've also attached a 'Handmade in Dorset' stamp which we'd like to go on there if possible, along with a shelf life symbol.

I am thinking the background colour of the labels will be either white or even brown paper colour. Perhaps it would be interesting to see it in both. UPDATE: We have decided on white background now, not brown.

The final design should denote handmade, organic, high quality, pure, yet quirky and original / unique. I am thinking perhaps a seemingly hand-drawn black leaf outline? Could fit the bill, but as I say, up to you. Something that says handmade yet professional.

I'd like to have the original Photoshop files from the winning designer so we can use them as a template for the rest of our horizontal labels.

Target Market(s)

Everyone that appreciates a good quality skincare product focusing on natural & organic. Price is mid-range to high

Industry/Entity Type

It Company

Requirements
Must have
• Must make the product look high quality & organic yet quirky and accessible. Must have our logo and the shelf life symbol and the writing as above.
Nice to have
• Nice to have the 'handmade' stamp attached, but not absolutely necessary if it doesn't fit within your design.

```html
<!DOCTYPE html>
<html lang="en">
<head>
<meta charset="utf-8">
<title>Gently Lumora – Whipped Body Butter Labels</title>
<link href="https://fonts.googleapis.com/css2?family=Lato:wght@300;400;700&family=Sriracha&display=swap" rel="stylesheet">
<style>
  :root {
    --paper: #ffffff;
    --frame: #cfcfcf;
    --ink: #555555;
    --ink-soft: #7a7a7a;
    --coral: #f06b61;
    --mango: #fcc813;
    --stamp: #7dbf7d;
    --on-blob: #ffffff;
  }
  * { box-sizing: border-box; margin: 0; padding: 0; }
  html, body {
    width: 1200px; height: 1200px; overflow: hidden;
    background: var(--paper);
  }
  .canvas { position: relative; width: 1200px; height: 1200px; }

  .label {
    position: absolute; left: 275px;
    width: 649px; height: 191px;
    border: 1px solid var(--frame);
    background: var(--paper);
    font-family: "Lato", sans-serif;
    color: var(--ink);
  }
  .label--mango { top: 367px; --accent: var(--mango); }
  .label--vanilla { top: 640px; --accent: var(--coral); }

  .ingredients {
    position: absolute; left: 10px; top: 12px; width: 190px;
    font-size: 8.6px; line-height: 11.2px; font-weight: 400;
    text-align: justify; color: var(--ink);
  }
  .ingredients strong { font-weight: 700; }
  .maker {
    position: absolute; left: 10px; top: 121px;
    font-size: 8.6px; line-height: 11.2px; color: var(--ink);
  }

  .blob { position: absolute; left: 231px; top: 0; width: 196px; height: 191px; }
  .blob svg { position: absolute; inset: 0; width: 100%; height: 100%; }
  .blob path { fill: var(--accent); }

  .front { position: absolute; inset: 0; text-align: center; color: var(--on-blob); }
  .brand {
    position: absolute; left: 0; right: 0; top: 22px;
    font-weight: 700; font-size: 16px; line-height: 17px; letter-spacing: 1px;
    text-transform: uppercase;
  }
  .product { position: absolute; left: 0; right: 0; font-weight: 300; }
  .product--organic { top: 78px; font-size: 17px; }
  .product--style { top: 99px; font-size: 12.6px; }
  .product--type { top: 118px; font-size: 15px; }
  .product--type span {
    display: inline-block; padding-bottom: 3px;
    border-bottom: 1px solid var(--on-blob);
  }
  .scent {
    position: absolute; left: 0; right: 0; top: 142px;
    font-family: "Sriracha", cursive; font-size: 17px;
  }

  .stamp { position: absolute; left: 416px; top: 101px; width: 60px; height: 54px; }

  .volume {
    position: absolute; left: 420px; top: 162px;
    font-size: 15px; font-weight: 300; color: var(--ink);
  }

  .claims { position: absolute; left: 501px; top: 55px; color: var(--ink-soft); }
  .claims__big { font-size: 23px; font-weight: 700; line-height: 26px; }
  .claims__line { font-size: 11.6px; line-height: 14.5px; font-weight: 400; }
  .claims__script {
    margin-top: 10px; font-family: "Sriracha", cursive;
    font-size: 12px; line-height: 14px; color: var(--ink-soft);
  }
  .claims__list { margin-top: 3px; font-size: 10.4px; line-height: 12.8px; }
</style>
</head>
<body>
<main class="canvas">

  <section class="label label--mango" aria-label="Mango smoothie label">
    <p class="ingredients"><strong>Ingredients (INCI):</strong> Organic Raw Shea Butter (Butyrospermum Parkii), Organic Raw Cocoa Butter (Theobroma Cacao), Monoi de Tahiti (Coconut (Cocos nucifera) oil (and) Tiare (Gardenia tahitensis) flower), Organic Sweet Almond Oil (Prunus Amygdalus Dulcis), Organic Madagascan Vanilla Extract (Vanillin).</p>
    <p class="maker">Handmade<br>by Gently Lumora Ltd<br>14 Quillfield Lane,<br>Bournemouth BH2 9RT, UK<br>Batch:</p>

    <div class="blob">
      <svg viewBox="0 0 196 191" aria-hidden="true"><path d="M98 3 C142 0 176 20 186 58 C194 90 191 122 180 150 C165 182 128 192 94 188 C56 186 18 172 9 138 C2 110 6 70 22 42 C40 14 66 5 98 3 Z"/></svg>
      <div class="front">
        <p class="brand">Gently<br>Lumora</p>
        <p class="product product--organic">ORGANIC</p>
        <p class="product product--style">POLYNESIAN WHIPPED</p>
        <p class="product product--type"><span>BODY BUTTER</span></p>
        <p class="scent">mango smoothie</p>
      </div>
    </div>

    <svg class="stamp" viewBox="0 0 60 54" aria-hidden="true"><circle cx="30" cy="27" r="24" fill="none" stroke="var(--stamp)" stroke-width="3"/></svg>
    <p class="volume">120ml</p>

    <div class="claims">
      <p class="claims__big">100%</p>
      <p class="claims__line">Natural and Organic<br>Intensely Moisturising</p>
      <p class="claims__script">made with</p>
      <p class="claims__list">Organic Shea<br>&amp; Cocoa Butters<br>&amp; exotic Monoi de Tahiti</p>
    </div>
  </section>

  <section class="label label--vanilla" aria-label="Vanilla bean label">
    <p class="ingredients"><strong>Ingredients (INCI):</strong> Organic Raw Shea Butter (Butyrospermum Parkii), Organic Raw Cocoa Butter (Theobroma Cacao), Monoi de Tahiti (Coconut (Cocos nucifera) oil (and) Tiare (Gardenia tahitensis) flower), Organic Sweet Almond Oil (Prunus Amygdalus Dulcis), Organic Madagascan Vanilla Extract (Vanillin).</p>
    <p class="maker">Handmade<br>by Gently Lumora Ltd<br>14 Quillfield Lane,<br>Bournemouth BH2 9RT, UK<br>Batch:</p>

    <div class="blob">
      <svg viewBox="0 0 196 191" aria-hidden="true"><path d="M98 3 C142 0 176 20 186 58 C194 90 191 122 180 150 C165 182 128 192 94 188 C56 186 18 172 9 138 C2 110 6 70 22 42 C40 14 66 5 98 3 Z"/></svg>
      <div class="front">
        <p class="brand">Gently<br>Lumora</p>
        <p class="product product--organic">ORGANIC</p>
        <p class="product product--style">POLYNESIAN WHIPPED</p>
        <p class="product product--type"><span>BODY BUTTER</span></p>
        <p class="scent">vanilla bean</p>
      </div>
    </div>

    <svg class="stamp" viewBox="0 0 60 54" aria-hidden="true"><circle cx="30" cy="27" r="24" fill="none" stroke="var(--stamp)" stroke-width="3"/></svg>
    <p class="volume">120ml</p>

    <div class="claims">
      <p class="claims__big">100%</p>
      <p class="claims__line">Natural and Organic<br>Intensely Moisturising</p>
      <p class="claims__script">made with</p>
      <p class="claims__list">Organic Shea<br>&amp; Cocoa Butters<br>&amp; exotic Monoi de Tahiti</p>
    </div>
  </section>

</main>
</body>
</html>
```